New Letterhead request for our Law Firm!

We are a small Estate Planning Firm who just got out logo redesigned. It's attached. We need some letterhead for our client welcome letters and so forth. Clean, bright, and approachable is our style. If you need the specifications for our color scheme or other versions of the logo file, we have those too. Visit our website to get an idea about our services/aesthetics:https://bramblecove.law/

Target Market(s)

Adults 30-80

Colors

Designer to choose colors to be used in the design.

Requirements
Must have
• Logo with color. Contact information

```html
<!DOCTYPE html>
<html lang="en">
<head>
<meta charset="utf-8">
<title>Bramblecove Law Firm – Letterhead</title>
<link href="https://fonts.googleapis.com/css2?family=Open+Sans:wght@400;600&display=swap" rel="stylesheet">
<style>
  :root {
    --backdrop: #e4e4e4;
    --paper: #ffffff;
    --ink: #4a4a4a;
    --ink-strong: #333333;
    --sage: #6f9e84;
    --charcoal: #4b4b4d;
    --watermark: #ececec;
    --on-band: #ffffff;
  }
  * { box-sizing: border-box; margin: 0; padding: 0; }
  html, body {
    width: 1040px; height: 1200px; overflow: hidden;
    background: var(--backdrop);
    font-family: "Open Sans", Arial, sans-serif;
  }
  .letterhead {
    position: absolute; left: 54px; top: 0;
    width: 932px; height: 1200px;
    background: var(--paper);
    color: var(--ink);
    box-shadow: 0 0 18px rgba(0,0,0,0.12);
    overflow: hidden;
  }
  .brand {
    position: absolute; top: 24px; left: 0; right: 0;
    display: flex; justify-content: center; align-items: center; gap: 10px;
  }
  .brand-dot {
    width: 52px; height: 52px; border-radius: 50%;
    border: 3px solid var(--sage);
  }
  .brand-name {
    font-weight: 600; font-size: 22px; color: var(--sage);
    letter-spacing: 1px; line-height: 1.1;
  }
  .letter {
    position: absolute; left: 87px; width: 753px;
    font-size: 14.5px; line-height: 18px;
  }
  .issue-date { top: 216px; }
  .recipient { top: 253px; }
  .salutation { top: 357px; }
  .body-copy { top: 411px; }
  .body-copy p {
    text-align: justify; line-height: 27px; margin-bottom: 27px;
    hyphens: auto;
  }
  .closing { top: 815px; }
  .signatory { top: 893px; }
  .signatory-name { font-size: 19px; font-weight: 600; color: var(--ink-strong); line-height: 26px; }
  .signatory-title { font-size: 14.5px; margin-top: 4px; }
  .watermark-mark {
    position: absolute; left: 596px; top: 772px;
    width: 330px; height: 330px; border-radius: 50%;
    background: var(--watermark);
  }
  .footer-bands { position: absolute; left: 0; bottom: 0; width: 932px; height: 58px; }
  .footer-contact {
    position: absolute; left: 92px; bottom: 7px;
    font-size: 18px; color: var(--on-band);
  }
  .footer-contact strong { font-weight: 600; }
  .footer-address {
    position: absolute; right: 96px; bottom: 4px;
    font-size: 18px; line-height: 22px; color: var(--on-band); text-align: right;
  }
</style>
</head>
<body>
  <main class="letterhead">
    <header class="brand">
      <span class="brand-dot"></span>
      <span class="brand-name">BRAMBLECOVE LAW FIRM</span>
    </header>

    <div class="watermark-mark" role="img" aria-label="Faint brand mark decoration"></div>

    <p class="letter issue-date">Issuing Date: May 5, 2018</p>
    <p class="letter recipient">Name Of Employee Mr. XYZABC<br>Address of Employee<br>Address Line 2 etc..</p>
    <p class="letter salutation">Dear Mr.XYZABC</p>

    <section class="letter body-copy">
      <p>Lorem Ipsum has been the industry's standard dummy text ever since the 1500s, when an unknown printer took a galley of type and scrambled it to make a type specimen book. It has survived not only five centuries, but also the leap into electronic typesetting, remaining essentially unchanged. It was popularised in the 1960s with the release of Letraset sheets containing Lorem Ipsum passages, and more recently with desktop publishing software like Aldus PageMaker including versions of Lorem Ipsum.</p>
      <p>Lorem Ipsum is simply dummy text of the printing and typesetting industry. Lorem Ipsum has been the industry's standard dummy text ever since the 1500s, when an unknown printer took a galley of type and scrambled it to make a type specimen book.</p>
      <p>It has survived not only five centuries, but also the leap into electronic typesetting, remaining essentially unchanged. It was popularised in the 1960s with the release of Letraset sheets containing Lorem IpsumIpsum passages.</p>
    </section>

    <p class="letter closing">Yours Sincerely</p>
    <div class="letter signatory">
      <p class="signatory-name">Daniel Whitaker</p>
      <p class="signatory-title">Managing Director</p>
    </div>

    <footer>
      <svg class="footer-bands" viewBox="0 0 932 58" aria-hidden="true">
        <polygon points="0,22 453,22 441,58 0,58" fill="var(--sage)"/>
        <polygon points="467,0 932,0 932,58 447,58" fill="var(--charcoal)"/>
      </svg>
      <p class="footer-contact"><strong>P:</strong> 555 014 2278 | www.bramblecove.law</p>
      <p class="footer-address">420 Linden Avenue, Suite 12<br>Fairbrook, MN 55990</p>
    </footer>
  </main>
</body>
</html>
```